Cool Landing page with email address sign up (mockups provided)

I need a landing page for a service that will send a weekly email to people who are looking for jobs in startups. On the landing page there is a call to action (submit button) to register their email address. The service is called VentureRoster and it is a side project to try to assist startup companies with hiring people.

I just want one single form field "Email".

The feeling I want to give people is one of adventure. Imagine the person is living in Gdansk Poland, they are a technical/IT expert and have dreams of making it big in a Startup in London. This is his big chance, this is going to allow him to do it! He's signing up to a big promise! It should be cool, professional, exciting.

A major influence should be:
http://copperkettlefair.example/

There should also be a call to tweet in a cool way like on (http://www.behindfounders.example/).

Look at this - taking a leap of faith, like this:
http://pagebloomkit.example/wp-content/uploads/2011/09/19.jpg

This is super with the colours - striking!:
http://hueparlor.example/

Fly your kit higher!:
http://tobiasvrenn.example/

If necessary use sex to sell:
http://pagebloomkit.example/wp-content/uploads/2011/09/24.jpg

Some original art would work:
http://pagebloomkit.example/wp-content/uploads/2011/09/fx_ss_group1_sm_filtered_0000s_0007_Layer-14.jpg

This is effective for a call to action, I'm looking to you to act!:
http://pagebloomkit.example/wp-content/uploads/2011/09/weblance.jpg
Take inspiration from:
http://www.behindfounders.example/
http://ventureroster.example/
http://foundersdaily.example/

***N.B.: I would prefer original art background over a photo

Also:
http://pixeljournalhub.example/inspiration/a-showcase-of-landing-pages-designed-for-conversion
especially:
http://pixeljournalhub.example/wp-content/uploads/2011/09/01-landing.jpg
http://pixeljournalhub.example/wp-content/uploads/2011/09/04-landing.jpg
http://pixeljournalhub.example/wp-content/uploads/2011/10/texture21.jpg

I really like the colouring from Coder Bulletin:
http://news.quillforge.example/

Reason: I'm going to be away for a few days so I won't have enough time to properly provide feedback.

The payment is now guaranteed. This project is a single page only.

I've added a few more example landing pages that I like.

I've now added the ventureroster logo image that should be used.

I've updated brief with more examples of what I'm looking for

Reason: I'm still progressing with candidate designs.

Target Market(s)

Technical people, english not being their native language. Ambitious to work in London/Dublin in a tech startup company. They want to receive a weekly emails with startup jobs in london or dublin.

Requirements
Must have
• Eyes must be drawn to the email registration form to get them to submit their email address. The background image or website theme should encourage their desires to work in the big city in exciting startup companies.

Should have a prompt to tweet (once pressed I'll do my own popup)

```html
<!DOCTYPE html>
<html lang="en">
<head>
<meta charset="utf-8">
<title>VentureRoster – Weekly startup jobs</title>
<link rel="stylesheet" href="https://fonts.googleapis.com/css2?family=Oregano&family=PT+Sans&family=Playfair+Display:ital@1&family=Ubuntu:wght@300&display=swap">
<style>
  :root {
    --header-top: #9e1010;
    --header-bottom: #5c0202;
    --header-edge: #3a0000;
    --page-black: #000000;
    --glow-cyan: #4fd2ff;
    --glow-blue: #1a6fc9;
    --glow-deep: #0a2346;
    --nav-dot: #f2d21a;
    --text-white: #ffffff;
    --heading-dark: #2c2c2c;
    --heading-muted: #9a9a9a;
    --panel-white: #ffffff;
    --field-border: #c9c9c9;
    --field-text: #555555;
    --button-top: #a9e04a;
    --button-bottom: #6cb51f;
    --button-text: #2d4a0a;
    --follow-orange: #f07a1a;
  }
  * { box-sizing: border-box; margin: 0; padding: 0; }
  html, body {
    width: 1200px; height: 727px; overflow: hidden;
    background: var(--page-black);
  }
  .page {
    position: relative; width: 1200px; height: 727px; overflow: hidden;
    background: var(--page-black);
  }
  .site-header {
    position: absolute; left: 0; top: 0; width: 1200px; height: 103px;
    background: linear-gradient(180deg, var(--header-top) 0%, #7d0808 60%, var(--header-bottom) 100%);
    border-bottom: 2px solid var(--header-edge);
  }
  .brand {
    position: absolute; left: 218px; top: 22px;
    font-family: "Ubuntu", sans-serif; font-weight: 300;
    font-size: 44px; letter-spacing: -0.5px;
    color: var(--text-white);
  }
  .main-nav {
    position: absolute; left: 684px; top: 67px;
    display: flex; align-items: center; gap: 15px;
    font-family: "PT Sans", sans-serif; font-size: 13px;
    color: var(--text-white); list-style: none;
  }
  .main-nav .dot {
    width: 8px; height: 8px; border-radius: 50%; background: var(--nav-dot);
  }
  .world-glow {
    position: absolute; left: 110px; top: 130px; width: 1000px; height: 600px;
    background:
      radial-gradient(ellipse 38% 30% at 50% 48%, rgba(120,230,255,0.55) 0%, rgba(40,140,230,0.35) 45%, transparent 75%),
      radial-gradient(ellipse 50% 45% at 50% 50%, var(--glow-blue) 0%, var(--glow-deep) 55%, transparent 80%);
    opacity: 0.9;
  }
  .follow {
    position: absolute; left: 778px; top: 118px;
    display: flex; align-items: center; gap: 12px;
  }
  .follow .mark {
    width: 44px; height: 44px; border-radius: 50%; background: var(--follow-orange);
  }
  .follow .label {
    font-family: "Playfair Display", serif; font-style: italic;
    font-size: 22px; color: var(--follow-orange);
  }
  .signup-panel {
    position: absolute; left: 314px; top: 251px; width: 527px; height: 327px;
    background: var(--panel-white);
    box-shadow: 0 0 6px rgba(0,0,0,0.6);
  }
  .signup-heading {
    position: absolute; left: 22px; top: 26px; width: 490px;
    font-family: "Oregano", cursive; font-size: 29px; line-height: 38px;
    color: var(--heading-dark); font-weight: 400;
  }
  .signup-heading .lead { font-size: 40px; color: var(--heading-muted); }
  .signup-form {
    position: absolute; left: 45px; top: 170px; width: 425px; height: 52px;
  }
  .email-field {
    width: 100%; height: 100%;
    border: 2px solid var(--field-border); border-radius: 26px;
    padding: 0 140px 0 18px;
    font-family: "PT Sans", sans-serif; font-size: 17px; color: var(--field-text);
    background: var(--panel-white);
  }
  .email-field::placeholder { color: var(--field-text); }
  .register-button {
    position: absolute; right: 0; top: 0; width: 120px; height: 52px;
    border: none; border-radius: 26px;
    background: linear-gradient(180deg, var(--button-top), var(--button-bottom));
    font-family: "PT Sans", sans-serif; font-size: 20px; color: var(--button-text);
  }
  .site-footer {
    position: absolute; left: 0; top: 688px; width: 1200px; text-align: center;
    font-family: "PT Sans", sans-serif; font-size: 10px; color: var(--text-white);
  }
</style>
</head>
<body>
<div class="page">
  <div class="world-glow" role="img" aria-label="Glowing dotted world map in electric blue light rays"></div>

  <header class="site-header">
    <div class="brand">ventureroster</div>
    <ul class="main-nav">
      <li>Details</li><li class="dot"></li>
      <li>Company</li><li class="dot"></li>
      <li>Media</li><li class="dot"></li>
      <li>Why StartUp?</li>
    </ul>
  </header>

  <div class="follow">
    <span class="mark"></span>
    <span class="label">Follow us</span>
  </div>

  <section class="signup-panel">
    <h1 class="signup-heading"><span class="lead">Sign up</span> now for a simple, free weekly email of the best startup jobs near you.</h1>
    <form class="signup-form">
      <input class="email-field" type="email" placeholder="Enter your email address">
      <button class="register-button" type="button">Register</button>
    </form>
  </section>

  <footer class="site-footer">© www.ventureroster.com | All Right Reserved</footer>
</div>
</body>
</html>
```